yourSmileCare Brookvale Business Card

Please design a two sided business card that is Elegant and Professional
Add subtle elegant patterns to suit Spot UV printing/ or raised printing

Name: Dr Marcus T. Fenwick
Qualification: BDSc (QLD)
Title: Dental Surgeon, Clinical Director
Company: yourSmileCare Brookvale
Phone: (02) 7593 2268
Address: Shop 7/18-20 Lindon Ave Brookvale 2097
email: info@yoursmilecarebrookvale.com.au
Facebook: chatterly.com/yoursmilecarebrookvale

Motto:
Quality dentistry you can trust

Description of services (not compulsory):
Preventative Dentistry | General Dentistry
Cosmetic Dentistry | Teeth Whitening
Crown and Bridge | Root Canal Therapy
Veneers | Clearvono | Orthodontics
Emergency Dental Care | After Hours

Personalised Treatment Plans
Transparent Fees

Please make sure card is elegant and professional

Target Market(s)

general population, patients,
Dental sales companies, other professions

Industry/Entity Type

Dental Clinic

Contact Information for Business Card

Name: Dr Marcus T. Fenwick
Qualification: BDSc (QLD)
Phone: (02) 7593 2268
Address: Shop 7/18-20 Lindon Ave Brookvale

Motto:

Description of services (not compulsory)

Transparent Fees

Image of dental surgery optional

Please make sure card is elegant and profession

Requirements
Must have
• Logo
• Name, Title (next to name), Business
• Phone, address, facbeook
• Must have stylish design to suit SPOT UV reflective printing
Nice to have
• Subtle elegant patterns which will have Spot UV on them when printed
• Colours to match logo colour
• Description of services
Should not have
• Small fonts that are hard to read
• DO NOT PUT IMAGES OF DENTAL INSTRUMENTS OR TEETH PLEASE

```html
<!DOCTYPE html>
<html lang="en">
<head>
<meta charset="utf-8">
<title>yourSmileCare Brookvale – Business Card</title>
<link href="https://fonts.googleapis.com/css2?family=Open+Sans:ital,wght@0,400;0,600;0,700;1,400;1,600&display=swap" rel="stylesheet">
<style>
  :root {
    --green: #6cc531;
    --green-deep: #0e7a2e;
    --green-lime: #a4e34a;
    --ink: #222222;
    --grey: #8a8a8a;
    --paper: #ffffff;
    --stage: #9c9c9c;
    --stage-light: #cfcfcf;
    --band: #111111;
  }
  * { box-sizing: border-box; margin: 0; padding: 0; }
  html, body { width: 1200px; height: 960px; overflow: hidden; }
  body {
    font-family: "Open Sans", Arial, sans-serif;
    background: radial-gradient(ellipse at 50% 40%, var(--stage-light), var(--stage));
    position: relative;
  }
  .card {
    position: absolute;
    left: 250px;
    width: 700px;
    height: 428px;
    border-radius: 6px;
    box-shadow: 0 10px 30px rgba(0,0,0,0.25);
    overflow: hidden;
  }
  /* Front side */
  .card--front { top: 32px; background: var(--paper); color: var(--ink); }
  .brand { position: absolute; left: 44px; top: 40px; color: var(--green); font-weight: 600; line-height: 1; }
  .brand__name { font-size: 36px; letter-spacing: -0.5px; }
  .brand__place { font-size: 20px; letter-spacing: 3px; margin-top: 6px; text-align: right; }
  .motto { position: absolute; left: 44px; top: 140px; font-size: 17px; font-style: italic; font-weight: 600; line-height: 1.3; }
  .band {
    position: absolute; left: 0; top: 238px; width: 290px; height: 44px;
    background: var(--band); border-radius: 0 22px 22px 0;
    color: var(--paper); font-size: 18px; font-weight: 600;
    display: flex; align-items: center; padding-left: 40px; white-space: nowrap;
  }
  .band__lead { color: var(--green); }
  .contact { position: absolute; left: 316px; top: 120px; width: 370px; }
  .contact__name { font-size: 25px; font-weight: 700; white-space: nowrap; }
  .contact__qual { font-size: 11px; color: var(--grey); font-weight: 400; margin-left: 6px; }
  .contact__title { font-size: 16px; margin-top: 2px; }
  .contact__phone { display: flex; align-items: center; gap: 10px; font-size: 28px; font-weight: 700; color: var(--green); margin: 14px 0 12px; }
  .contact__row { display: flex; align-items: center; gap: 10px; font-size: 15px; margin-bottom: 8px; white-space: nowrap; }
  .contact__row strong { font-weight: 700; }
  .icon-dot { width: 24px; height: 24px; border-radius: 50%; background: var(--green); flex: none; display: flex; align-items: center; justify-content: center; }
  .contact__address { font-size: 15px; margin-top: 12px; white-space: nowrap; }

  /* Back side */
  .card--back { top: 500px; background: linear-gradient(125deg, var(--green-deep) 0%, var(--green) 60%, var(--green-lime) 100%); color: var(--paper); }
  .services-badge { position: absolute; left: 82px; top: 48px; text-align: center; }
  .services-badge__mark { width: 84px; height: 84px; border-radius: 50%; border: 3px solid var(--paper); background: rgba(255,255,255,0.18); margin: 0 auto; }
  .services-badge__label { font-size: 17px; margin-top: 8px; }
  .services-badge__label strong { font-weight: 700; }
  .brand--light { left: 44px; top: 250px; color: var(--paper); }
  .services { position: absolute; left: 300px; top: 56px; width: 380px; text-align: center; font-size: 17px; line-height: 1.55; }
  .promises { position: absolute; left: 300px; top: 300px; list-style: none; font-size: 17px; }
  .promises li { display: flex; align-items: center; gap: 12px; margin-bottom: 12px; }
  .tick { width: 24px; height: 24px; border-radius: 50%; background: var(--paper); display: flex; align-items: center; justify-content: center; flex: none; }
</style>
</head>
<body>

<section class="card card--front" aria-label="Business card front">
  <div class="brand">
    <div class="brand__name">yourSmileCare</div>
    <div class="brand__place">Brookvale</div>
  </div>
  <p class="motto">Quality dentistry<br>you can trust</p>
  <div class="band"><span class="band__lead">yourSmileCare</span>&nbsp;Brookvale</div>

  <div class="contact">
    <div class="contact__name">Dr Marcus T. Fenwick<span class="contact__qual">BDSc (QLD)</span></div>
    <div class="contact__title">Dental Surgeon, Clinical Director</div>
    <div class="contact__phone">
      <svg width="22" height="26" viewBox="0 0 22 26" aria-hidden="true"><path d="M6 2 L10 8 L7 11 C8 15 10 18 13 20 L16 17 L21 21 L18 25 C9 24 2 15 2 6 Z" fill="var(--green)"/></svg>
      (02) 7593 2268
    </div>
    <div class="contact__row">
      <span class="icon-dot"><svg width="14" height="10" viewBox="0 0 14 10" aria-hidden="true"><rect x="0.5" y="0.5" width="13" height="9" fill="none" stroke="#fff"/><path d="M0.5 0.5 L7 6 L13.5 0.5" fill="none" stroke="#fff"/></svg></span>
      <span>info@yoursmilecarebrookvale.com.au</span>
    </div>
    <div class="contact__row">
      <span class="icon-dot"><svg width="14" height="14" viewBox="0 0 14 14" aria-hidden="true"><circle cx="7" cy="7" r="6" fill="none" stroke="#fff"/><path d="M1 7 H13 M7 1 C4 4 4 10 7 13 M7 1 C10 4 10 10 7 13" fill="none" stroke="#fff"/></svg></span>
      <span>yoursmilecarebrookvale.com.au</span>
    </div>
    <div class="contact__row">
      <span class="icon-dot"></span>
      <span>chatterly.com/<strong>yoursmilecarebrookvale</strong></span>
    </div>
    <div class="contact__address">Shop 7/18-20 Lindon Ave Brookvale 2097</div>
  </div>
</section>

<section class="card card--back" aria-label="Business card back">
  <div class="services-badge">
    <div class="services-badge__mark" role="img" aria-label="Services emblem"></div>
    <div class="services-badge__label">Our <strong>Services</strong></div>
  </div>
  <div class="brand brand--light">
    <div class="brand__name">yourSmileCare</div>
    <div class="brand__place">Brookvale</div>
  </div>
  <p class="services">
    Preventative Dentistry | General Dentistry<br>
    Cosmetic Dentistry | Teeth Whitening<br>
    Crown and Bridge | Root Canal Therapy<br>
    Veneers | Clearvono | Orthodontics<br>
    Emergency Dental Care | After Hours
  </p>
  <ul class="promises">
    <li><span class="tick"><svg width="12" height="10" viewBox="0 0 12 10" aria-hidden="true"><path d="M1 5 L4.5 8.5 L11 1.5" fill="none" stroke="var(--green)" stroke-width="2.2"/></svg></span>Personalised Treatment Plans</li>
    <li><span class="tick"><svg width="12" height="10" viewBox="0 0 12 10" aria-hidden="true"><path d="M1 5 L4.5 8.5 L11 1.5" fill="none" stroke="var(--green)" stroke-width="2.2"/></svg></span>Transparent Fees</li>
  </ul>
</section>

</body>
</html>
```